Hula-Hoop dance entertainment sales and instruction by twirl-spinette needs a business card

I need a 2 sided business card that is square (although this is not an absolute )for my self employed business as an independent artist. my business name is "Twirl-Spinette" I teach how to hula-hoop classes, make and sell hula-hoops, provided entertainment at kids birthday parties, community events, corporate events and perform at artistic dance shows.
I would like to see spirals or curved lines in the card, and I would like the card to be seen as fun, spunky, flair and eye catching.

the card could double as a tag to go on the hoops i sell,

Target Market(s)

women age 20 - 50

Industry/Entity Type

Entertainment

Requirements
Must have
• Minna Traversi
www.twirlspinette.example
555.734.2619
Nice to have
• I would like my image to be on one side of the card. so people can recognize me!

```html
<!DOCTYPE html>
<html lang="en">
<head>
<meta charset="utf-8">
<title>Minna Traversi — Hoop Dance Card</title>
<link rel="stylesheet" href="https://fonts.googleapis.com/css2?family=Griffy&family=PT+Sans:wght@400;700&display=swap">
<style>
  :root {
    --card-lavender: #a0a4d4;
    --ink: #000000;
  }
  * { margin: 0; padding: 0; box-sizing: border-box; }
  html, body {
    width: 1200px;
    height: 1200px;
    overflow: hidden;
    background: var(--card-lavender);
  }
  .card {
    position: relative;
    width: 1200px;
    height: 1200px;
    background: var(--card-lavender);
    border: 9px solid var(--ink);
    color: var(--ink);
    text-align: center;
  }
  .card__name {
    position: absolute;
    top: 38px;
    left: 0;
    width: 100%;
    font-family: "Griffy", cursive;
    font-size: 132px;
    line-height: 1.1;
    letter-spacing: 4px;
    font-weight: 400;
  }
  .card__rule {
    position: absolute;
    left: 146px;
    width: 890px;
    height: 4px;
    background: var(--ink);
  }
  .card__rule--top { top: 258px; }
  .card__rule--bottom { top: 922px; }
  .card__services {
    position: absolute;
    top: 296px;
    left: 0;
    width: 100%;
    list-style: none;
    font-family: "PT Sans", sans-serif;
    font-size: 49px;
    line-height: 66px;
    font-weight: 400;
  }
  .card__contact {
    position: absolute;
    top: 960px;
    left: 0;
    width: 100%;
    font-family: "PT Sans", sans-serif;
    font-weight: 700;
  }
  .card__web {
    font-size: 60px;
    line-height: 82px;
  }
  .card__phone {
    font-size: 68px;
    line-height: 82px;
    letter-spacing: 1px;
  }
</style>
</head>
<body>
  <main class="card">
    <h1 class="card__name">Minna Traversi</h1>
    <div class="card__rule card__rule--top"></div>
    <ul class="card__services">
      <li>Hoop Classes</li>
      <li>Hoop Jams</li>
      <li>Private Lessons</li>
      <li>Custom hula-hoops for adults and kids</li>
      <li>Performances</li>
      <li>Hoop Making Workshops</li>
      <li>Birthday Parties</li>
      <li>Corporate Event Entertainment</li>
      <li>and more!</li>
    </ul>
    <div class="card__rule card__rule--bottom"></div>
    <div class="card__contact">
      <p class="card__web">www.twirlspinette.example</p>
      <p class="card__phone">555.734.2619</p>
    </div>
  </main>
</body>
</html>
```